Car finance company business card

Create a nice business card for our car financing company , Visit our website www.brookmilefinance.com for the phone number and idea of the company look. Please do not be afraid to be creative. Name on card Is Marc-Olivier Dussault and phone number is on our website adress of business is
27816 Boulevard Des-Ormeaux,
Mirabel, QC H4R 2B6

```html
<!DOCTYPE html>
<html lang="fr">
<head>
<meta charset="utf-8">
<title>Brookmile Finance – Business Card</title>
<link rel="stylesheet" href="https://fonts.googleapis.com/css2?family=Lato:wght@400;700;900&display=swap">
<style>
  :root {
    --page-bg: #e4e4e4;
    --card-bg: #2f2e2e;
    --card-bg-light: #3a3939;
    --accent: #e9802b;
    --text-light: #f2f2f2;
    --text-muted: #c9c9c9;
  }
  * { box-sizing: border-box; margin: 0; padding: 0; }
  html, body {
    width: 1200px;
    height: 1200px;
    overflow: hidden;
    background: var(--page-bg);
    font-family: "Lato", sans-serif;
  }
  .business-card {
    position: absolute;
    left: 100px;
    top: 314px;
    width: 1000px;
    height: 572px;
    border-radius: 6px;
    background: radial-gradient(ellipse at 55% 30%, var(--card-bg-light), var(--card-bg) 70%);
    color: var(--text-light);
  }
  .brand {
    position: absolute;
    left: 0;
    right: 0;
    top: 120px;
    display: flex;
    justify-content: center;
    align-items: center;
    gap: 22px;
  }
  .brand-mark {
    width: 52px;
    height: 52px;
    border-radius: 50%;
    background: var(--accent);
    flex: none;
  }
  .brand-name {
    font-weight: 900;
    font-size: 60px;
    letter-spacing: 1px;
    color: var(--text-light);
    text-transform: uppercase;
    line-height: 1;
  }
  .contact {
    position: absolute;
    left: 0;
    right: 0;
    top: 262px;
    text-align: center;
  }
  .contact-name {
    font-weight: 700;
    font-size: 27px;
    color: var(--accent);
    text-transform: uppercase;
    letter-spacing: 0.5px;
  }
  .contact-role {
    font-size: 23px;
    color: var(--text-muted);
    margin-top: 2px;
  }
  .contact-icons {
    display: flex;
    justify-content: center;
    gap: 12px;
    margin: 12px 0 10px;
  }
  .contact-icons svg { width: 30px; height: 30px; }
  .contact-line {
    font-size: 24px;
    color: var(--text-muted);
    line-height: 1.3;
  }
  .contact-address {
    font-weight: 700;
    font-size: 25px;
    color: var(--text-light);
    margin-top: 14px;
  }
</style>
</head>
<body>
  <div class="business-card">
    <div class="brand">
      <span class="brand-mark"></span>
      <span class="brand-name">Brookmile Finance</span>
    </div>

    <div class="contact">
      <p class="contact-name">Marc-Olivier Dussault</p>
      <p class="contact-role">manager</p>
      <div class="contact-icons">
        <svg viewBox="0 0 30 30" aria-label="phone">
          <circle cx="15" cy="15" r="13" fill="none" stroke="var(--accent)" stroke-width="2"/>
          <path d="M11 9.5 l2.5 -0.5 l1.2 3 l-1.6 1.2 q1 2.5 3.2 3.6 l1.3 -1.5 l3 1.3 l-0.6 2.6 q-6.5 0.5 -9 -9.7z" fill="var(--accent)"/>
        </svg>
        <svg viewBox="0 0 30 30" aria-label="email">
          <circle cx="15" cy="15" r="13" fill="none" stroke="var(--accent)" stroke-width="2"/>
          <rect x="8.5" y="10.5" width="13" height="9" rx="1" fill="var(--accent)"/>
          <path d="M8.5 11 l6.5 5 l6.5 -5" fill="none" stroke="var(--card-bg)" stroke-width="1.4"/>
        </svg>
        <svg viewBox="0 0 30 30" aria-label="website">
          <circle cx="15" cy="15" r="13" fill="none" stroke="var(--accent)" stroke-width="2"/>
          <circle cx="15" cy="15" r="7" fill="none" stroke="var(--accent)" stroke-width="1.5"/>
          <ellipse cx="15" cy="15" rx="3" ry="7" fill="none" stroke="var(--accent)" stroke-width="1.3"/>
          <line x1="8" y1="15" x2="22" y2="15" stroke="var(--accent)" stroke-width="1.3"/>
        </svg>
      </div>
      <p class="contact-line">+(514) - 555 - 0172</p>
      <p class="contact-line">info@brookmilefinance.com</p>
      <p class="contact-line">www.brookmilefinance.com</p>
      <p class="contact-address">27816 Boulevard Des-Ormeaux, Mirabel, QC H4R 2B6</p>
    </div>
  </div>
</body>
</html>
```